High-end construction company needs a business card design

We need a modern looking business card that draws people in, is memorable and looks so good people will want to sick it on their fridges.
On the first side what is needed are:
Logo
My name - Tomas Verbelk
Title - Managing Director
Website - www.kravel.co.uk
Email - tomas@kravel.co.uk
Telephone - 020 5194 6381
Mobile - 07845319027
On the back side was is needed is a list of all the services we provide:
-Kitchen Renovations
-Bathroom Renovations
-House Renovations
-Garage Conversions
-Extensions
-Loft Conversions
-Conservatories
-Carpentry
-Tiling
-Electrical
-Plumbing & Heating
-Bricklaying
-Landscaping
-Decorating
-Plastering
We would like the colours to be the same shades as on the logo with grey or black for the words.
Target Market(s)
Anyone who needs building work done
Contact Information for Business Card
This business card is for a construction company which strives to deliver excellent service and quality.
The look and feel of the card should represent this.
Requirements
Must have
- On the first side what is needed are:
Logo
My name - Tomas Verbelk
Title - Managing Director
Website - www.kravel.co.uk
Email - tomas@kravel.co.uk
Telephone - 020 5194 6381
Mobile - 07845319027
Nice to have
- Cool looking features

```html
<!DOCTYPE html>
<html lang="en">
<head>
<meta charset="utf-8">
<title>Kravel Construction – Business Card</title>
<link href="https://fonts.googleapis.com/css2?family=Jost:ital,wght@0,400;0,600;0,700;1,400&display=swap" rel="stylesheet">
<style>
  :root {
    --brand-green: #6cbf3c;
    --card-grey: #6d6e71;
    --text-grey: #58595b;
    --paper: #ffffff;
    --backdrop: #dfe8e0;
  }
  * { margin: 0; padding: 0; box-sizing: border-box; }
  html, body {
    width: 1200px; height: 927px; overflow: hidden;
    background: var(--backdrop);
    font-family: "Jost", "Futura", sans-serif;
  }
  .canvas { position: relative; width: 1200px; height: 927px; }
  .card {
    position: absolute; top: 205px;
    width: 286px; height: 514px;
  }
  .card--front { left: 278px; background: var(--paper); }
  .card--back { left: 636px; background: var(--card-grey); }

  .brand {
    position: absolute; top: 52px; right: 32px;
    text-align: right;
    color: var(--brand-green);
    font-weight: 700;
    font-size: 26px; line-height: 1.05;
    letter-spacing: 0.5px;
  }
  .brand__sub { display: block; font-size: 11px; letter-spacing: 1.6px; text-transform: uppercase; }

  .contact { position: absolute; left: 34px; top: 284px; color: var(--text-grey); }
  .contact__name { color: var(--brand-green); font-weight: 600; font-size: 19px; line-height: 26px; margin-bottom: 2px; }
  .contact__line { font-size: 15.5px; line-height: 23px; }
  .contact__label { color: var(--brand-green); display: inline-block; width: 16px; }
  .rule { width: 19px; height: 2px; background: var(--brand-green); }
  .contact .rule { margin: 13px 0 16px; }
  .contact__web { color: var(--brand-green); font-size: 15.5px; line-height: 23px; }

  .services { position: absolute; right: 28px; top: 114px; text-align: right; }
  .services__title { color: var(--brand-green); font-size: 15.5px; line-height: 22px; }
  .services .rule { margin: 10px 0 12px auto; }
  .services__list { list-style: none; }
  .services__list li {
    color: #ffffff; font-style: italic; font-size: 13.5px; line-height: 22.2px;
  }
</style>
</head>
<body>
<main class="canvas">
  <section class="card card--front" aria-label="Front of business card">
    <div class="brand">Kravel<span class="brand__sub">Construction</span></div>
    <div class="contact">
      <p class="contact__name">Tomas Verbelk</p>
      <p class="contact__line">Managing Director</p>
      <p class="contact__line"><span class="contact__label">m</span>078-4531 9027</p>
      <p class="contact__line"><span class="contact__label">e</span>tomas@kravel.co.uk</p>
      <div class="rule"></div>
      <p class="contact__line"><span class="contact__label">t</span>020 5194 6381</p>
      <div class="rule"></div>
      <p class="contact__web">www.kravel.co.uk</p>
    </div>
  </section>

  <section class="card card--back" aria-label="Back of business card">
    <div class="services">
      <p class="services__title">Our services</p>
      <div class="rule"></div>
      <ul class="services__list">
        <li>Kitchen Renovations</li>
        <li>Bathroom Renovations</li>
        <li>House Renovations</li>
        <li>Garage Conversions</li>
        <li>Extensions</li>
        <li>Loft Conversions</li>
        <li>Conservatories</li>
        <li>Carpentry</li>
        <li>Tiling</li>
        <li>Electrical</li>
        <li>Plumbing &amp; Heating</li>
        <li>Bricklaying</li>
        <li>Landscaping</li>
        <li>Decorating</li>
        <li>Plastering</li>
      </ul>
    </div>
  </section>
</main>
</body>
</html>
```